Electronic Music Artist needs an Album Cover

DRELL is an electronic musician from Boston, Massachusetts. He needs an album cover that captures the essence of his music. The album is called Lanterns, which represents his experiences growing up, positive and negative. He would like to see designs that involves color and creativity. Attached are some examples of artworks that DRELL likes. He also included a few of his original photos (optional to use. Using a photo will not effect his final decision!), and his logo.

Colors

Designer to choose colors to be used in the design.

Requirements
Must have
• My project must have the text "Lanterns" and "DRELL", and the logo (attached in the files). The logo should not be the main subject of the artwork. Everything must look aesthetically pleasing.
Nice to have
• It would be nice to have some sort of creative graphic design (see example album covers for reference). Also, in one of the references, there is a column on the left hand side with some text in it. That could be cool to include, but without the asian text.
Should not have
• The project should not have any other language besides English.

```html
<!DOCTYPE html>
<html lang="en">
<head>
<meta charset="utf-8">
<title>DRELL — Lanterns</title>
<link rel="stylesheet" href="https://fonts.googleapis.com/css2?family=Inter:wght@700;900&display=swap">
<style>
  :root {
    --ink: #000000;
    --sky: #29a8e0;
    --sky-deep: #1e8fcc;
    --sky-pale: #4fc0ea;
    --ember: #e8643a;
    --ember-deep: #d9532e;
    --rose: #d2508a;
    --moss: #3fae5a;
    --mist: rgba(178, 224, 246, 0.72);
    --steel: #a3a3a8;
  }
  html, body {
    margin: 0;
    padding: 0;
    width: 1200px;
    height: 1200px;
    overflow: hidden;
    background: var(--ink);
  }
  .cover {
    position: relative;
    width: 1200px;
    height: 1200px;
    background: var(--ink);
    overflow: hidden;
  }
  .side-column {
    position: absolute;
    left: 0;
    top: 0;
    width: 400px;
    height: 1200px;
    background: var(--ink);
  }
  .city-photo {
    position: absolute;
    left: 400px;
    top: 0;
    width: 800px;
    height: 1200px;
    background:
      radial-gradient(ellipse 130px 190px at 94% 38%, rgba(232, 100, 58, 0.95), rgba(232, 100, 58, 0) 75%),
      radial-gradient(ellipse 70px 200px at 39% 22%, rgba(63, 174, 90, 0.55), rgba(63, 174, 90, 0) 75%),
      radial-gradient(ellipse 90px 60px at 26% 48%, rgba(232, 100, 58, 0.8), rgba(232, 100, 58, 0) 75%),
      radial-gradient(ellipse 170px 330px at 64% 83%, rgba(217, 83, 46, 0.7), rgba(210, 80, 138, 0) 75%),
      radial-gradient(ellipse 140px 300px at 30% 80%, rgba(210, 80, 138, 0.55), rgba(210, 80, 138, 0) 75%),
      radial-gradient(ellipse 380px 120px at 70% 27%, rgba(232, 100, 58, 0.45), rgba(232, 100, 58, 0) 75%),
      radial-gradient(ellipse 110px 260px at 95% 85%, rgba(232, 100, 58, 0.5), rgba(232, 100, 58, 0) 75%),
      linear-gradient(180deg, var(--sky) 0%, var(--sky) 18%, var(--sky-pale) 40%, var(--sky-deep) 70%, var(--sky) 100%);
  }
  .type-layer {
    position: absolute;
    left: 0;
    top: 0;
    width: 1200px;
    height: 1200px;
  }
  .artist-name,
  .label-mark {
    font-family: "Inter", "Helvetica Neue", Arial, sans-serif;
    font-weight: 700;
    fill: var(--steel);
  }
  .artist-name { font-size: 80px; letter-spacing: -1px; }
  .label-mark { font-size: 40px; }
  .album-title {
    font-family: "Inter", "Helvetica Neue", Arial, sans-serif;
    font-weight: 900;
    font-size: 250px;
    letter-spacing: -6px;
  }
  .title-solid { fill: var(--sky); }
  .title-veil { fill: var(--mist); }
</style>
</head>
<body>
  <main class="cover">
    <section class="side-column"></section>

    <div class="city-photo" role="img" aria-label="Aerial city skyline photo processed in vivid cyan with orange, magenta and green highlights on the towers"></div>

    <svg class="type-layer" viewBox="0 0 1200 1200" aria-label="DRELL — Lanterns">
      <defs>
        <clipPath id="clip-column"><rect x="0" y="0" width="400" height="1200"/></clipPath>
        <clipPath id="clip-photo"><rect x="400" y="0" width="800" height="1200"/></clipPath>
      </defs>
      <text class="artist-name" x="200" y="173" text-anchor="middle">DRELL</text>
      <text class="label-mark" x="200" y="1072" text-anchor="middle">DRELL</text>
      <text class="album-title title-solid" x="0" y="688" textLength="1200" lengthAdjust="spacingAndGlyphs" clip-path="url(#clip-column)">Lanterns</text>
      <text class="album-title title-veil" x="0" y="688" textLength="1200" lengthAdjust="spacingAndGlyphs" clip-path="url(#clip-photo)" aria-hidden="true">Lanterns</text>
    </svg>
  </main>
</body>
</html>
```